Covid19 Poster for workplaces

Create a poster on how to protect yourself from Corona virus at work.
We are a workplace wellbeing company. We have just re-branded so we need to fit in with our brand. We like clean and fresh, slightly amusing is ok if it will draw attention but it's an important topic. A4 and A3 please.

Content:

Headline: Lower the risk of COVID 19 in the workplace.

BE WELL

Bring your own cup - don’t share cups and food.
Elbow tap instead of handshakes and kisses
Wash your hands often - with soap.
Elbow or tissues when you cough or sneeze then straight in the bin
Leave your face alone after touching shared surfaces
Leave your bugs at home if you’re feeling unwell.

Call health line if you have a cough, a high temperature and shortness of breath. 0800 472 9160

Based on recommendations from ZPK and QLN

Target Market(s)

Employees - so anyone

Other font styles liked:
• Use the closest font to the brand documents

Requirements
Should not have
• Clip art

```html
<!DOCTYPE html>
<html lang="en">
<head>
<meta charset="utf-8">
<title>Lower the risk of COVID-19 in the workplace</title>
<link rel="stylesheet" href="https://fonts.googleapis.com/css2?family=Montserrat:wght@300;500;700;800;900&display=swap">
<style>
  :root {
    --navy: #2d3592;
    --blue: #2a7ccf;
    --lavender: #8088bf;
    --white: #ffffff;
    --yellow: #ffd400;
    --photo-a: #7b8aa6;
    --photo-b: #c9a27c;
    --virus-a: #3f5f8a;
    --virus-b: #5c8fd0;
  }
  * { margin: 0; padding: 0; box-sizing: border-box; }
  html, body { width: 848px; height: 1200px; overflow: hidden; }
  body { font-family: "Montserrat", sans-serif; color: var(--white); }

  .poster {
    position: relative;
    width: 848px;
    height: 1200px;
    overflow: hidden;
    background: linear-gradient(135deg, var(--navy) 0%, #2f4ba0 45%, var(--blue) 100%);
  }

  .art { position: absolute; inset: 0; width: 848px; height: 1200px; }

  .headline {
    position: absolute;
    left: 200px;
    top: 70px;
    font-weight: 900;
    font-size: 45px;
    line-height: 53px;
    letter-spacing: 0.09em;
    text-transform: uppercase;
  }

  .tips {
    position: absolute;
    left: 166px;
    top: 262px;
    width: 640px;
    list-style: none;
  }
  .tip {
    position: absolute;
    left: 0;
    display: flex;
    align-items: center;
    font-weight: 500;
    font-size: 22px;
    line-height: 29px;
    letter-spacing: 0.05em;
  }
  .tip:nth-child(1) { top: 0; }
  .tip:nth-child(2) { top: 75px; }
  .tip:nth-child(3) { top: 130px; }
  .tip:nth-child(4) { top: 185px; }
  .tip:nth-child(5) { top: 263px; }
  .tip:nth-child(6) { top: 340px; }
  .tip-icon { flex: none; width: 26px; height: 16px; margin-right: 12px; }

  .health-line {
    position: absolute;
    left: 244px;
    top: 718px;
    width: 277px;
    font-weight: 800;
    font-size: 19.5px;
    line-height: 35.5px;
    letter-spacing: 0.06em;
    text-transform: uppercase;
    text-align: justify;
  }

  .phone {
    position: absolute;
    left: 238px;
    top: 905px;
    width: 300px;
    color: var(--yellow);
    font-weight: 900;
    font-size: 54px;
    line-height: 58px;
    letter-spacing: 0.03em;
  }

  .source {
    position: absolute;
    left: 241px;
    top: 1043px;
    font-weight: 500;
    font-size: 22px;
    line-height: 31.5px;
    letter-spacing: 0.05em;
  }
</style>
</head>
<body>
<main class="poster">
  <svg class="art" viewBox="0 0 848 1200" aria-hidden="false">
    <defs>
      <linearGradient id="virus-fill" x1="0" y1="0" x2="1" y2="1">
        <stop offset="0" stop-color="var(--virus-a)"/>
        <stop offset="1" stop-color="var(--virus-b)"/>
      </linearGradient>
      <linearGradient id="portrait-fill" x1="0" y1="0" x2="1" y2="1">
        <stop offset="0" stop-color="var(--photo-a)"/>
        <stop offset="1" stop-color="var(--photo-b)"/>
      </linearGradient>
    </defs>

    <path class="virus-image" role="img" aria-label="Close-up image of coronavirus particles"
          fill="url(#virus-fill)"
          d="M0 0 L262 0 Q300 45 268 102 L100 312 Q76 338 50 314 L0 268 Z"/>

    <text class="word-corona" transform="translate(130 1175) rotate(-90)"
          font-family="Montserrat, sans-serif" font-weight="900" font-size="150"
          fill="var(--lavender)" textLength="720" lengthAdjust="spacingAndGlyphs">CORONA</text>
    <text class="word-virus" transform="translate(210 1155) rotate(-90)"
          font-family="Montserrat, sans-serif" font-weight="300" font-size="146"
          fill="var(--white)" textLength="435" lengthAdjust="spacingAndGlyphs">VIRUS</text>

    <path class="portrait-image" role="img" aria-label="Photo of a woman wearing a surgical face mask"
          fill="url(#portrait-fill)"
          d="M740 1200 L604 1095 A160 160 0 1 1 848 889 L848 1200 Z"/>
  </svg>

  <h1 class="headline">Lower the risk of<br>COVID-19 in the<br>workplace</h1>

  <ul class="tips">
    <li class="tip"><svg class="tip-icon" viewBox="0 0 26 16"><path fill="var(--yellow)" d="M7 15 L1 8 A3.6 3.6 0 0 1 7 3 A3.6 3.6 0 0 1 13 8 Z M19 15 L13 8 A3.6 3.6 0 0 1 19 3 A3.6 3.6 0 0 1 25 8 Z"/></svg><span>Bring your own cup - don’t share cups and<br>food</span></li>
    <li class="tip"><svg class="tip-icon" viewBox="0 0 26 16"><path fill="var(--yellow)" d="M7 15 L1 8 A3.6 3.6 0 0 1 7 3 A3.6 3.6 0 0 1 13 8 Z M19 15 L13 8 A3.6 3.6 0 0 1 19 3 A3.6 3.6 0 0 1 25 8 Z"/></svg><span>Elbow tap instead of handshakes and kisses</span></li>
    <li class="tip"><svg class="tip-icon" viewBox="0 0 26 16"><path fill="var(--yellow)" d="M7 15 L1 8 A3.6 3.6 0 0 1 7 3 A3.6 3.6 0 0 1 13 8 Z M19 15 L13 8 A3.6 3.6 0 0 1 19 3 A3.6 3.6 0 0 1 25 8 Z"/></svg><span>Wash your hands often - with soap</span></li>
    <li class="tip"><svg class="tip-icon" viewBox="0 0 26 16"><path fill="var(--yellow)" d="M7 15 L1 8 A3.6 3.6 0 0 1 7 3 A3.6 3.6 0 0 1 13 8 Z M19 15 L13 8 A3.6 3.6 0 0 1 19 3 A3.6 3.6 0 0 1 25 8 Z"/></svg><span>Elbow or tissues when you cough or sneeze<br>then straight in the bin</span></li>
    <li class="tip"><svg class="tip-icon" viewBox="0 0 26 16"><path fill="var(--yellow)" d="M7 15 L1 8 A3.6 3.6 0 0 1 7 3 A3.6 3.6 0 0 1 13 8 Z M19 15 L13 8 A3.6 3.6 0 0 1 19 3 A3.6 3.6 0 0 1 25 8 Z"/></svg><span>Leave your face alone after touching shared<br>surfaces</span></li>
    <li class="tip"><svg class="tip-icon" viewBox="0 0 26 16"><path fill="var(--yellow)" d="M7 15 L1 8 A3.6 3.6 0 0 1 7 3 A3.6 3.6 0 0 1 13 8 Z M19 15 L13 8 A3.6 3.6 0 0 1 19 3 A3.6 3.6 0 0 1 25 8 Z"/></svg><span>Leave your bugs at home if you’re feeling<br>unwell</span></li>
  </ul>

  <p class="health-line">Call health line if you have a cough, a high temperature and shortness of breath</p>

  <p class="phone">0800 472<br>9160</p>

  <p class="source">Based on<br>recommendations<br>from ZPK and QLN</p>
</main>
</body>
</html>
```